plivant-compatible banner ad set and associated landing page design

This is the message that the banner should communicate:
"Get Paid to Save the Planet - Solar Pays You Up to $750+ Every Year for Use of Your Roof"
BANNER SIZE:  300x250 would be great. (After choosing the winner, we will pay additional money to create new versions indifferent sizes as a follow-on work.)
BANNER FORMAT:  Could be an animated GIF, static JPG HTML 5, video, your call.
As for design guidelines for the ad and landing page, follow design guidance at: http://qr-tx41.vendolix.com/rs/clickharvo/images/10%20blunders%20layout_final%20(1).pdf
The banner ad will be used on the Plivant Ad network and should have a call to action to get the user to click to the landing page. The call to action can be two buttons within the banner ad:
"I Care About Planet Earth"
"Don't Care"
Clicking anywhere on the banner ad will drive traffic to the landing page.
On the landing page, we want a design that we can implement in sitelumora.com to capture the following information:
- Street Number and Street Name of My Home
- My Zip Code
- Name of My Electric Utility
- My Typical Monthly Electric Bill Amount is:
- How Much I'd Like to Earn From Solar Per-Year?
After the user fills out the above, the following questions drop down:
First Name
Last Name
Email Address
Phone Number
At the end of the data entry portion of the landing page, there should be a "call to action" button.
LANDING PAGE FORMAT:  Photoshop or jpg format or html5 format would be great.

Updates
Target Market(s)
home owners
Industry/Entity Type
Home Improvement
Requirements
Nice to have
- Follow design guidance at: http://qr-tx41.vendolix.com/rs/clickharvo/images/10%20blunders%20layout_final%20(1).pdf

```html
<!DOCTYPE html>
<html lang="en">
<head>
<meta charset="utf-8">
<title>Sunvera Solar – Banner Set</title>
<link rel="stylesheet" href="https://fonts.googleapis.com/css2?family=Lato:wght@400;700;900&display=swap">
<style>
  :root {
    --page-bg: #ffffff;
    --label: #222222;
    --navy: #1d2f45;
    --green: #7dc242;
    --green-dark: #3f7a2a;
    --sky-top: #3f8fd0;
    --sky-mid: #8cc3ea;
    --roof: #c8623a;
    --roof-dark: #8a3c22;
    --panel: #2b4a6e;
    --strip: #d8d8d8;
    --black: #0b0b0b;
    --white: #ffffff;
  }
  * { box-sizing: border-box; margin: 0; padding: 0; }
  html, body { width: 1200px; height: 2828px; overflow: hidden; background: var(--page-bg); }
  body { font-family: "Lato", sans-serif; position: relative; }

  .frame-label {
    position: absolute; left: 0; width: 1200px; text-align: center;
    font-size: 50px; font-weight: 400; color: var(--label); letter-spacing: 1px;
  }
  .banner {
    position: absolute; left: 168px; width: 848px; height: 706px; overflow: hidden;
  }
  .rooftop-photo {
    position: absolute; left: 0; right: 0; bottom: 88px;
    background:
      linear-gradient(180deg, var(--sky-top) 0%, var(--sky-mid) 55%, var(--panel) 70%, var(--roof) 82%, var(--roof-dark) 100%);
  }
  .banner--intro .rooftop-photo,
  .banner--offer .rooftop-photo { top: 0; }
  .banner--cta .rooftop-photo { top: 260px; background: linear-gradient(180deg, var(--sky-mid) 0%, var(--panel) 45%, var(--roof) 72%, var(--roof-dark) 100%); }

  .brand-strip {
    position: absolute; left: 0; right: 0; bottom: 0; height: 88px; background: var(--strip);
    display: flex; align-items: center; padding-left: 28px;
  }
  .brand-name {
    font-family: "Lato", sans-serif; font-weight: 900; font-size: 40px; color: var(--green-dark);
    letter-spacing: 2px; display: flex; align-items: center; gap: 12px;
  }
  .brand-mark { width: 26px; height: 26px; background: var(--green-dark); }

  .headline {
    position: absolute; left: 48px; top: 44px; color: var(--navy);
    font-weight: 900; font-size: 88px; line-height: 1.08;
  }
  .subhead {
    position: absolute; left: 40px; right: 30px; top: 40px; color: var(--navy);
    font-weight: 700; font-size: 50px; line-height: 1.25;
  }
  .subhead .amount { color: var(--green-dark); }

  .feature-icons { position: absolute; right: 40px; bottom: 112px; display: flex; gap: 56px; }
  .feature-icon {
    width: 144px; height: 144px; background: rgba(235,235,235,0.85);
    display: flex; align-items: center; justify-content: center;
  }

  .choice-panel {
    position: absolute; left: 0; right: 0; top: 0; height: 260px; background: var(--black);
    padding: 44px 0 0 80px;
  }
  .choice {
    display: flex; align-items: center; gap: 36px; color: var(--green);
    font-size: 54px; font-weight: 400; height: 72px; margin-bottom: 40px;
  }
  .choice-box { width: 44px; height: 44px; background: #e6e6e6; border-radius: 6px; }

  .go-button {
    position: absolute; right: 28px; bottom: 14px; width: 392px; height: 104px;
    background: var(--black); border: 3px solid #444; border-radius: 6px;
    display: flex; align-items: center; justify-content: center; gap: 24px;
    color: var(--white); font-size: 54px; font-weight: 400; letter-spacing: 1px;
  }
</style>
</head>
<body>

<div class="frame-label" style="top:44px">FRAME 1</div>
<section class="banner banner--intro" style="top:144px">
  <div class="rooftop-photo" role="img" aria-label="Rooftop with solar panels under a sunny blue sky"></div>
  <h1 class="headline">GET PAID<br>TO GO SOLAR !</h1>
  <div class="feature-icons">
    <div class="feature-icon">
      <svg width="104" height="104" viewBox="0 0 104 104"><circle cx="52" cy="52" r="52" fill="#3f7a2a"/><path d="M52 22 L80 46 H72 V78 H32 V46 H24 Z" fill="none" stroke="#fff" stroke-width="5" stroke-linejoin="round"/><text x="52" y="70" text-anchor="middle" font-family="Lato, sans-serif" font-weight="900" font-size="28" fill="#fff">$</text></svg>
    </div>
    <div class="feature-icon">
      <svg width="104" height="104" viewBox="0 0 104 104"><circle cx="52" cy="52" r="52" fill="#3f7a2a"/><rect x="28" y="26" width="38" height="52" fill="none" stroke="#fff" stroke-width="4"/><path d="M28 43 H66 M28 60 H66 M47 26 V78" stroke="#fff" stroke-width="3"/><path d="M74 40 V78" stroke="#fff" stroke-width="5"/></svg>
    </div>
  </div>
  <div class="brand-strip"><span class="brand-name"><span class="brand-mark"></span>SUNVERA</span></div>
</section>

<div class="frame-label" style="top:948px">FRAME 2</div>
<section class="banner banner--offer" style="top:1072px">
  <div class="rooftop-photo" role="img" aria-label="Rooftop with solar panels under a sunny blue sky"></div>
  <h2 class="subhead">Solar Pays You Up to <span class="amount">$750+</span> Every Year for Use of Your Roof</h2>
  <div class="feature-icons">
    <div class="feature-icon">
      <svg width="104" height="104" viewBox="0 0 104 104"><circle cx="52" cy="52" r="52" fill="#3f7a2a"/><path d="M52 22 L80 46 H72 V78 H32 V46 H24 Z" fill="none" stroke="#fff" stroke-width="5" stroke-linejoin="round"/><text x="52" y="70" text-anchor="middle" font-family="Lato, sans-serif" font-weight="900" font-size="28" fill="#fff">$</text></svg>
    </div>
    <div class="feature-icon">
      <svg width="104" height="104" viewBox="0 0 104 104"><circle cx="52" cy="52" r="52" fill="#3f7a2a"/><rect x="28" y="26" width="38" height="52" fill="none" stroke="#fff" stroke-width="4"/><path d="M28 43 H66 M28 60 H66 M47 26 V78" stroke="#fff" stroke-width="3"/><path d="M74 40 V78" stroke="#fff" stroke-width="5"/></svg>
    </div>
  </div>
  <div class="brand-strip"><span class="brand-name"><span class="brand-mark"></span>SUNVERA</span></div>
</section>

<div class="frame-label" style="top:1836px">FRAME 3</div>
<section class="banner banner--cta" style="top:1988px">
  <div class="choice-panel">
    <div class="choice"><span class="choice-box"></span>I Care About Planet Earth</div>
    <div class="choice"><span class="choice-box"></span>Don't Care</div>
  </div>
  <div class="rooftop-photo" role="img" aria-label="Rooftop with solar panels and a rooftop vent unit"></div>
  <div class="brand-strip"><span class="brand-name"><span class="brand-mark"></span>SUNVERA</span></div>
  <div class="go-button">GO SOLAR
    <svg width="28" height="44" viewBox="0 0 28 44"><path d="M4 4 L22 22 L4 40" fill="none" stroke="#7dc242" stroke-width="8"/></svg>
  </div>
</section>

</body>
</html>
```